Farm Entrance Sign Design for Estate - Maplewick Meadow Farm

I am seeking a sign to hang where you turn in my driveway to my farm. The name of the farm is "Maplewick Meadow Farm". The sign/logo does not need the work "Farm" in it necessarily. The sign should be simple, clean, elegant.

I will attach some basic signs that are of the quality I am seeking. I will also attach a view of the farm entrance. I do not want the sign to compete with the landscape. This is in an area of estate type farms with horses and high end homes.

We are a cattle farm. But don't necessarily have to have cow on sign.

Font styles to use
Sans Serif

Colors

Designer to choose colors to be used in the design.

Requirements
Nice to have
• I prefer a clean font...nothing fancy

```html
<!DOCTYPE html>
<html lang="en">
<head>
<meta charset="utf-8">
<title>The Maplewick Meadow – Entrance Sign</title>
<link href="https://fonts.googleapis.com/css2?family=Montserrat:wght@700&display=swap" rel="stylesheet">
<style>
  :root {
    --backdrop: #eeeeee;
    --sign-border: #000000;
    --sign-cream: #f7edcf;
    --frame-line: #1e1a17;
    --ridge-mist: #c9bfa9;
    --ridge-mid: #6b645b;
    --ridge-dark: #1e1a17;
    --lettering: #000000;
  }
  * { margin: 0; padding: 0; box-sizing: border-box; }
  html, body {
    width: 1200px;
    height: 1200px;
    overflow: hidden;
    background: var(--backdrop);
  }
  .canvas {
    position: relative;
    width: 1200px;
    height: 1200px;
  }
  .entrance-sign {
    position: absolute;
    left: 50px;
    top: 187px;
    width: 1100px;
    height: 825px;
    background: var(--sign-cream);
    border: 27px solid var(--sign-border);
    overflow: hidden;
  }
  .ridge-scene {
    position: absolute;
    left: 0;
    right: 0;
    bottom: 0;
    height: 45%;
    background: linear-gradient(
      to bottom,
      var(--sign-cream) 0%,
      var(--ridge-mist) 18%,
      var(--ridge-mid) 45%,
      var(--ridge-dark) 72%,
      var(--ridge-dark) 100%
    );
  }
  .inner-frame {
    position: absolute;
    left: 35px;
    top: 23px;
    right: 35px;
    bottom: 38px;
    border: 12px solid var(--frame-line);
  }
  .sign-name {
    position: absolute;
    left: 0;
    right: 0;
    font-family: "Montserrat", sans-serif;
    font-weight: 700;
    color: var(--lettering);
    text-align: center;
    line-height: 1;
    letter-spacing: 0.01em;
  }
  .sign-name--article {
    top: 220px;
    font-size: 72px;
  }
  .sign-name--first {
    top: 340px;
    font-size: 118px;
  }
  .sign-name--second {
    top: 494px;
    font-size: 118px;
  }
</style>
</head>
<body>
  <main class="canvas">
    <section class="entrance-sign" aria-label="The Maplewick Meadow entrance sign">
      <div class="ridge-scene" role="img" aria-label="Layered misty mountain ridges fading from cream into dark silhouette"></div>
      <div class="inner-frame"></div>
      <p class="sign-name sign-name--article">THE</p>
      <p class="sign-name sign-name--first">MAPLEWICK</p>
      <p class="sign-name sign-name--second">MEADOW</p>
    </section>
  </main>
</body>
</html>
```